Super elegant, crisp & clean Business card design required

We recently upgraded our branding - which is on our website - tavorelstudio.com

I would like a simple, yet elegant, clean business card design please.

The font of my logo is Cinzel - and because of the natural colour - it's best to have this on a black background.

I would like to have the back of the business card - with simply my logo.

PLEASE DO NOT SUBMIT A COMPLICATED / UNCLEAN DESIGN

Industry/Entity Type

Business

Contact Information for Business Card

Dalvik Ostrander Photography

Font styles to use
Other font styles liked:
• Cinzel

Requirements
Must have
• A backpage with nothing but my logo
• Simple design - stands out
Should not have
• Colour that dont align with my logo
• Over complicated '/ non symmetrical design

```html
<!DOCTYPE html>
<html lang="en">
<head>
<meta charset="UTF-8">
<title>Dalvik Ostrander Photography – Business Card</title>
<link rel="stylesheet" href="https://fonts.googleapis.com/css2?family=Cinzel:wght@400;700&display=swap">
<style>
  :root {
    --backdrop: #3a2a20;
    --card-black: #0d0d0d;
    --gold: #a89a7a;
    --gold-soft: #8f8468;
  }
  * { box-sizing: border-box; margin: 0; padding: 0; }
  html, body {
    width: 1200px;
    height: 864px;
    overflow: hidden;
  }
  body {
    background: var(--backdrop);
    font-family: "Cinzel", serif;
    color: var(--gold);
  }
  .canvas {
    position: relative;
    width: 1200px;
    height: 864px;
    display: flex;
    align-items: center;
    justify-content: center;
    gap: 40px;
  }
  .card {
    position: relative;
    width: 520px;
    height: 300px;
    background: var(--card-black);
    box-shadow: 0 14px 30px rgba(0, 0, 0, 0.45);
  }
  .card-frame {
    position: absolute;
    inset: 14px;
    border: 2px solid var(--gold);
  }

  /* Back side: name only */
  .card-back {
    display: flex;
    flex-direction: column;
    align-items: center;
    justify-content: center;
  }
  .back-name {
    position: relative;
    font-weight: 400;
    font-size: 32px;
    letter-spacing: 1px;
    line-height: 1.1;
    text-align: center;
  }
  .back-tagline {
    position: relative;
    margin-top: 6px;
    font-weight: 400;
    font-size: 14px;
    letter-spacing: 10px;
    text-align: center;
    padding-left: 10px;
  }

  /* Front side: name + contact */
  .card-front {
    padding: 48px 56px 0;
  }
  .front-name {
    position: relative;
    text-align: center;
    font-weight: 400;
    font-size: 30px;
    letter-spacing: 1px;
    line-height: 1.1;
  }
  .front-tagline {
    position: relative;
    text-align: center;
    font-size: 18px;
    letter-spacing: 2px;
    color: var(--gold-soft);
    margin-top: 2px;
  }
  .contact-list {
    position: relative;
    list-style: none;
    margin-top: 36px;
    margin-left: 18px;
    font-size: 14px;
    line-height: 1.75;
    color: var(--gold-soft);
  }
  .contact-label {
    font-weight: 700;
    color: var(--gold);
  }
</style>
</head>
<body>
  <main class="canvas">
    <section class="card card-back" aria-label="Card back">
      <div class="card-frame"></div>
      <p class="back-name">DALVIK OSTRANDER</p>
      <p class="back-tagline">PHOTOGRAPHY</p>
    </section>

    <section class="card card-front" aria-label="Card front">
      <div class="card-frame"></div>
      <h1 class="front-name">Dalvik Ostrander</h1>
      <p class="front-tagline">Photography</p>
      <ul class="contact-list">
        <li><span class="contact-label">Phone</span> : 555-214-7730</li>
        <li><span class="contact-label">Mail</span> : info@tavorelstudio.com</li>
        <li><span class="contact-label">Web</span> : www.tavorelstudio.com</li>
      </ul>
    </section>
  </main>
</body>
</html>
```